Ad Design for a child care centre

Bright Pebbles Child Care Centre offers a safe, nurturing environment where your child will get the attention and care that he or she needs. Our ratio of children to adults is always within state guidelines - and often even higher - to make certain each child receives top-quality care
We are also state licensed as a Child Care facility and have met or exceeded all health and safety guidelines.
3-5 year Kinder Funded Program
Story Time
Show and Tell
Puzzles and Games
Computer Time
Arts and Crafts
Music
Pre-Reading Activities
And much more
You can rest assured that your child will be cared for with the most kindness, love and respect. We believe all children are precious gifts and we treat them as though they are our own.
Full-time, part-time, Half days, Before, after-school schedules are available.
To learn more, contact us today! 03 9481 -0576 or info@brightpebbles.example.au

```html
<!DOCTYPE html>
<html lang="en">
<head>
<meta charset="utf-8">
<title>Bright Pebbles Child Care and Kinder – Flyer</title>
<link rel="stylesheet" href="https://fonts.googleapis.com/css2?family=Merriweather:ital,wght@0,300;0,400;0,700;0,900;1,400;1,700&display=swap">
<style>
  :root {
    --purple: #8e2b8f;
    --green: #8cc63f;
    --orange: #f7941d;
    --pink: #ec008c;
    --white: #ffffff;
    --ink: #1d1d1d;
    --backdrop: #4a423b;
  }
  * { box-sizing: border-box; margin: 0; padding: 0; }
  html, body {
    width: 1200px; height: 941px; overflow: hidden;
    background: var(--backdrop);
    font-family: "Merriweather", Georgia, serif;
  }
  .flyer {
    position: absolute; left: 302px; top: 48px;
    width: 596px; height: 845px;
    background: var(--white); overflow: hidden;
  }
  .header-bg { position: absolute; left: 0; top: 0; width: 596px; height: 300px; }
  .flyer-title {
    position: absolute; top: 26px; width: 100%; text-align: center;
    color: var(--white); font-size: 31px; font-weight: 700; font-style: italic;
  }
  .flyer-tagline {
    position: absolute; top: 70px; width: 100%; text-align: center;
    color: var(--white); font-size: 19px; font-weight: 300; letter-spacing: .3px;
  }
  .flyer-tagline strong { font-weight: 700; }
  .web-pill {
    position: absolute; top: 116px; left: 186px; width: 224px; height: 24px;
    background: var(--white); border-radius: 12px;
    color: var(--ink); font-size: 13.5px; text-align: center; line-height: 24px;
  }
  .intro {
    position: absolute; top: 148px; left: 10px; width: 580px;
    color: var(--white); font-size: 14.6px; line-height: 20.5px; letter-spacing: .25px;
  }
  .intro em { font-style: italic; }
  .lead {
    position: absolute; top: 305px; left: 28px; width: 320px;
    font-size: 12px; line-height: 14.5px; color: var(--ink);
  }
  .activities {
    position: absolute; top: 360px; left: 16px; list-style: none;
    font-size: 19.5px; font-weight: 700; line-height: 31px;
  }
  .activities .green { color: var(--green); }
  .activities .orange { color: var(--orange); }
  .activities .pink { color: var(--pink); }
  .activities .purple { color: var(--purple); }
  .activities .dark { color: var(--ink); }
  .photo { position: absolute; }
  .photo-group   { left: 360px; top: 300px; width: 220px; height: 90px;  background: linear-gradient(135deg,#8a7a5a,#c5b391 60%,#7b8f62); }
  .photo-toddler { left: 229px; top: 396px; width: 90px;  height: 98px;  background: linear-gradient(160deg,#f3eef0,#e8c6cf 60%,#d7d0c7); }
  .photo-infant  { left: 324px; top: 396px; width: 95px;  height: 98px;  background: linear-gradient(160deg,#bfa79b,#e2c1b6 55%,#9a7e86); }
  .photo-party   { left: 425px; top: 396px; width: 155px; height: 134px; background: linear-gradient(150deg,#b36f93,#e39bc2 50%,#7a9659); }
  .photo-siblings{ left: 264px; top: 500px; width: 155px; height: 140px; background: linear-gradient(150deg,#8b7a55,#c95b52 50%,#e0c3b2); }
  .photo-family  { left: 425px; top: 538px; width: 155px; height: 102px; background: linear-gradient(150deg,#7d8a70,#d8c2a6 50%,#5c5f87); }
  .promise {
    position: absolute; top: 645px; left: 0; width: 596px; height: 80px;
    background: var(--orange); color: var(--white);
    font-size: 15px; font-weight: 700; line-height: 19.5px; letter-spacing: .2px;
    padding: 13px 20px 0; text-align: center;
  }
  .schedules {
    position: absolute; top: 725px; left: 0; width: 272px; height: 120px;
    background: var(--pink); color: var(--white); text-align: center;
    padding-top: 27px; font-size: 13.5px; line-height: 17.5px;
  }
  .schedules strong { font-weight: 700; display: block; letter-spacing: .4px; }
  .schedules span { font-weight: 300; letter-spacing: .3px; }
  .contact {
    position: absolute; top: 725px; left: 272px; width: 324px; height: 120px;
    background: var(--purple); color: var(--white); text-align: center; padding-top: 22px;
  }
  .contact-cta { font-size: 13.5px; font-weight: 300; letter-spacing: .3px; }
  .contact-phone { font-size: 17px; font-weight: 700; margin-top: 6px; letter-spacing: .5px; }
  .contact-email { font-size: 17px; font-weight: 700; font-style: italic; margin-top: 2px; }
</style>
</head>
<body>
  <article class="flyer">
    <svg class="header-bg" viewBox="0 0 596 300" aria-hidden="true">
      <rect x="0" y="0" width="596" height="295" fill="#8cc63f"/>
      <path d="M0 0 H596 V96 Q300 130 0 102 Z" fill="#8e2b8f"/>
    </svg>
    <h1 class="flyer-title">Bright Pebbles Child Care and Kinder</h1>
    <p class="flyer-tagline">we are not just a <strong>Child Care</strong> centre we are <strong>Family</strong></p>
    <div class="web-pill">www.brightpebbles.example.au</div>
    <p class="intro"><em><strong>Bright Pebbles Child Care Centre</strong></em> offers a <em>safe, nurturing environment</em> where your child will get the attention and care that he or she needs. Our ratio of children to adults is always within state guidelines - and often even higher - to make certain each child receives <em>top-quality care</em><br>We are also state licensed as a Child Care facility and have met or exceeded all health and safety guidelines.</p>

    <p class="lead">At Bright Pebbles Child Care your child will participate in developmentally appropriate activities throughout the day, such as:</p>
    <ul class="activities">
      <li class="purple">3-5Year Kinder Funded program</li>
      <li class="green">Story Time</li>
      <li class="orange">Show and Tell</li>
      <li class="pink">Puzzles and Games</li>
      <li class="purple">Computer Time</li>
      <li class="green">Arts and Crafts</li>
      <li class="orange">Music</li>
      <li class="pink">Pre-Reading Activities</li>
      <li class="dark">and Much More</li>
    </ul>

    <div class="photo photo-group" role="img" aria-label="Photo of children seated around an outdoor activity table"></div>
    <div class="photo photo-toddler" role="img" aria-label="Photo of a toddler sitting with balloons"></div>
    <div class="photo photo-infant" role="img" aria-label="Photo of a baby lying on a play mat"></div>
    <div class="photo photo-party" role="img" aria-label="Photo of children in costumes playing outdoors"></div>
    <div class="photo photo-siblings" role="img" aria-label="Photo of a smiling girl holding a baby"></div>
    <div class="photo photo-family" role="img" aria-label="Photo of a carer with a group of children in the garden"></div>

    <p class="promise">You can rest assured that your child will be cared for with the most kindness, love and respect. We believe all children are precious gifts and we treat them as though they are our own.</p>

    <div class="schedules">
      <strong>FULL-TIME, PART-TIME,<br>HALF DAYS,<br>BEFORE &amp; AFTER-SCHOOL</strong>
      <span>schedules are available</span>
    </div>
    <div class="contact">
      <p class="contact-cta">to learn more, contact us today!</p>
      <p class="contact-phone">03 9481 -0576</p>
      <p class="contact-email">info@brightpebbles.example.au</p>
    </div>
  </article>
</body>
</html>
```